Brimble Diecast Torvel Collectables Website

looking for a vibrant web site marketplace built for diecast car enthusiasts to buy, sell, and trade with ease. Whether you're looking to showcase your own collection or discover rare and exciting models, our site makes the process simple and enjoyable. Clients can browse a curated inventory of high‑quality diecast cars, connect with fellow collectors, and find the perfect pieces to expand their collection. With a smooth user experience and a community-driven spirit, we’re the go‑to destination for anyone passionate about diecast cars.

Target Market(s)

diecast collectors

Industry/Entity Type

Diecast Collectables

Coding

Coded - Design and coding required

Number of Pages Required

3 page

Font styles to use
Sans Serif

Colors
EE7325
F08F49
F5BC92
FAE3D3
FDF4ED

Requirements
Must have
• Cool look and feel. Woo commerce page to post and sell my inventory
Nice to have
• page for users to post their cars or looking for trades.
Should not have
• look cheap

```html
<!DOCTYPE html>
<html lang="en">
<head>
<meta charset="utf-8">
<title>Brimble Diecast — The Curated Circuit</title>
<link rel="stylesheet" href="https://fonts.googleapis.com/css2?family=Space+Grotesk:wght@500;600;700&family=Manrope:wght@400;500;600;700;800&display=swap">
<style>
:root{
  --orange:#EE7325;
  --orange-2:#F08F49;
  --peach:#F5BC92;
  --sand:#FAE3D3;
  --cream:#FDF4ED;
  --rust:#A8470E;
  --rust-deep:#8E3A0A;
  --hero-bg:#FCEEE3;
  --soft-bg:#FFF8F4;
  --ink:#23150E;
  --muted:#5B4A40;
  --line:#EADBD0;
  --dark:#2B1A11;
}
*{box-sizing:border-box;margin:0;padding:0}
html,body{width:1200px;height:3889px;overflow:hidden}
body{position:relative;background:#fff;font-family:"Manrope",sans-serif;color:var(--ink)}
.abs{position:absolute}
.head{font-family:"Space Grotesk",sans-serif;font-weight:700;letter-spacing:-0.02em}

.brand-top{left:10px;top:20px;display:flex;align-items:center;gap:12px}
.brand-dot{width:64px;height:64px;border-radius:50%;background:var(--rust)}
.brand-top span{font-family:"Space Grotesk",sans-serif;font-weight:700;font-size:26px;color:var(--rust)}

.nav{left:0;top:242px;width:1200px;height:78px;background:#fff;border-bottom:1px solid var(--line)}
.nav .logo{left:47px;top:20px;display:flex;align-items:center;gap:10px}
.nav .logo i{width:38px;height:38px;border-radius:50%;background:var(--rust);display:block}
.nav .logo span{font-family:"Space Grotesk",sans-serif;font-weight:700;font-size:21px;color:var(--rust)}
.nav-links{left:345px;top:28px;display:flex;gap:30px;font-size:14px;font-weight:600}
.nav-links a{color:var(--ink);text-decoration:none;padding-bottom:6px}
.nav-links a.active{color:var(--rust);border-bottom:2px solid var(--rust)}
.search{left:818px;top:23px;width:238px;height:33px;background:var(--cream);border-radius:8px;display:flex;align-items:center;gap:8px;padding:0 12px;font-size:12px;color:#9B8A80}
.nav-icon{top:27px}

.hero{left:0;top:320px;width:1200px;height:813px;background:var(--hero-bg)}
.tag{left:47px;top:133px;background:var(--orange-2);color:#5A2208;font-size:10px;font-weight:800;letter-spacing:.1em;padding:4px 10px;border-radius:12px}
.hero h1{left:47px;top:180px;width:540px;font-size:66px;line-height:1.08;color:var(--ink)}
.hero h1 em{font-style:normal;color:var(--rust)}
.hero p{left:47px;top:503px;width:520px;font-size:19px;line-height:1.4;color:var(--muted)}
.btn-primary{background:linear-gradient(90deg,#B8480C,#E0701F);color:#fff;font-weight:700;border-radius:6px;display:flex;align-items:center;justify-content:center;box-shadow:0 10px 22px rgba(200,90,20,.28)}
.btn-ghost{background:#fff;border:1px solid var(--line);color:var(--ink);font-weight:600;border-radius:6px;display:flex;align-items:center;justify-content:center}
.hero .b1{left:47px;top:627px;width:205px;height:53px;font-size:15px}
.hero .b2{left:269px;top:627px;width:154px;height:53px;font-size:15px}
.hero-photo{left:623px;top:79px;width:531px;height:654px;border-radius:22px;background:radial-gradient(ellipse 60% 30% at 55% 52%,#D9A21E 0%,#9C7316 35%,rgba(40,38,35,0) 70%),linear-gradient(180deg,#161616,#3B3B3B);box-shadow:0 20px 40px rgba(0,0,0,.25)}
.stat{background:rgba(255,255,255,.94);border-radius:14px;box-shadow:0 12px 30px rgba(0,0,0,.14);padding:22px 22px}
.stat b{display:block;font-family:"Space Grotesk",sans-serif;font-size:22px;color:var(--rust)}
.stat small{font-size:10px;letter-spacing:.12em;color:#8A7C72;font-weight:600}
.stat.s1{left:1030px;top:124px;width:138px;height:94px}
.stat.s2{left:594px;top:593px;width:175px;height:95px}

.featured{left:0;top:1133px;width:1200px;height:745px;background:var(--soft-bg)}
.sec-title{font-size:45px;color:var(--ink)}
.sec-sub{font-size:16px;color:var(--muted)}
.featured .sec-title{left:47px;top:86px}
.featured .sec-sub{left:47px;top:152px}
.arrow{top:132px;width:44px;height:44px;border-radius:50%;background:#fff;border:1px solid var(--line);display:flex;align-items:center;justify-content:center}
.card{top:236px;width:254px}
.card .photo{position:relative;height:317px;border-radius:4px}
.card .badge{position:absolute;left:14px;top:12px;font-size:9px;font-weight:700;padding:4px 10px;border-radius:10px;color:#fff}
.card .fav{position:absolute;right:14px;bottom:16px;width:36px;height:36px;background:#fff;border-radius:8px;display:flex;align-items:center;justify-content:center}
.card .maker{margin-top:16px;font-size:12.5px;color:var(--muted)}
.card h3{font-family:"Manrope",sans-serif;font-size:18px;font-weight:700;margin-top:5px;white-space:nowrap}
.card .row{display:flex;justify-content:space-between;align-items:center;margin-top:10px}
.card .price{font-family:"Space Grotesk",sans-serif;font-weight:600;font-size:20px;color:var(--rust)}
.card .scale{font-size:11px;color:var(--muted)}

.hub{left:0;top:1878px;width:1200px;height:887px;background:var(--hero-bg)}
.hub .sec-title{left:47px;top:86px}
.hub .sec-sub{left:47px;top:152px}
.feature{left:47px;top:236px;width:541px;height:561px;border-radius:22px;background:radial-gradient(ellipse 25% 35% at 50% 42%,#4A4A4A,rgba(0,0,0,0) 70%),linear-gradient(180deg,#424242,#2E241E 85%);overflow:hidden}
.feature .mc{left:30px;top:362px;background:var(--orange);color:#3A1404;font-size:10px;font-weight:700;padding:3px 10px;border-radius:3px}
.feature h3{left:30px;top:392px;width:480px;font-size:34px;line-height:1.12;color:#fff}
.feature .by{left:30px;top:496px;display:flex;align-items:center;gap:12px;color:#EDE2DA;font-size:14px}
.feature .by i{width:36px;height:36px;border-radius:8px;background:#6C5A4E;border:2px solid var(--orange);display:block}
.talk{left:612px;top:236px;width:542px;height:272px;border-radius:22px;background:var(--sand);overflow:hidden}
.talk .corner{right:0;top:0;width:120px;height:118px;background:#F2D0B8;border-bottom-left-radius:10px}
.talk h4{left:30px;top:86px;width:470px;font-family:"Space Grotesk",sans-serif;font-size:21px;line-height:1.4;font-weight:700}
.talk p{left:30px;top:158px;width:400px;font-size:14px;line-height:1.6;color:var(--muted)}
.talk a{left:30px;top:214px;font-size:14px;font-weight:700;color:var(--rust);display:flex;gap:6px;align-items:center}
.mini-card{width:258px;height:265px;border-radius:18px}
.verify{left:612px;top:532px;background:#fff;box-shadow:0 6px 20px rgba(150,80,30,.07)}
.summit{left:894px;top:532px;background:var(--rust)}
.mini-card .ic{left:22px;top:22px;width:36px;height:36px;border-radius:8px;display:flex;align-items:center;justify-content:center}
.mini-card h5{left:22px;top:80px;width:215px;font-size:16px;line-height:1.3;font-weight:800}
.mini-card p{left:22px;top:140px;width:215px;font-size:10.5px;line-height:1.7}
.verify .lab{right:22px;top:24px;font-size:8.5px;letter-spacing:.08em;color:#9B8A80;font-weight:600}
.summit .reg{left:22px;top:212px;width:214px;height:28px;background:#fff;color:var(--rust);font-size:11px;font-weight:800;letter-spacing:.1em;display:flex;align-items:center;justify-content:center;border-radius:3px}

.cta{left:47px;top:2854px;width:1107px;height:428px;background:var(--dark);border-radius:40px;text-align:center;color:#fff}
.cta h2{position:absolute;left:0;right:0;top:100px;font-size:54px}
.cta p{position:absolute;left:180px;right:180px;top:184px;font-size:18.5px;line-height:1.45;color:#D9CCC3}
.cta .c1{left:269px;top:290px;width:296px;height:62px;font-size:16px;letter-spacing:.04em}
.cta .c2{left:580px;top:290px;width:257px;height:62px;font-size:16px;font-weight:700;border:1px solid #6B564A;border-radius:6px;display:flex;align-items:center;justify-content:center}

.foot-logo{left:47px;top:3508px;font-family:"Space Grotesk",sans-serif;font-weight:700;font-size:20px}
.foot-about{left:47px;top:3562px;width:245px;font-size:13px;line-height:1.65;color:var(--muted)}
.foot-social{left:47px;top:3666px;display:flex;gap:14px}
.foot-col{top:3508px}
.foot-col h6{font-size:11px;letter-spacing:.12em;font-weight:800;margin-bottom:20px}
.foot-col li{list-style:none;font-size:13.5px;color:var(--muted);margin-bottom:15px}
.foot-bottom{left:47px;top:3781px;width:1107px;display:flex;justify-content:space-between;font-size:12px;color:var(--muted)}
.foot-bottom .right{display:flex;gap:30px;font-size:10.5px;letter-spacing:.14em;color:#9B8A80}
</style>
</head>
<body>

<div class="abs brand-top"><i class="brand-dot"></i><span>BRIMBLE DIECAST</span></div>

<header class="abs nav">
  <div class="abs logo"><i></i><span>BRIMBLE</span></div>
  <nav class="abs nav-links"><a class="active">Marketplace</a><a>Collector Hub</a><a>Community</a></nav>
  <div class="abs search">
    <svg width="15" height="15" viewBox="0 0 24 24" fill="none" stroke="#5B4A40" stroke-width="2.4"><circle cx="10" cy="10" r="6.5"/><path d="M15 15l5 5"/></svg>
    Search the circuit...
  </div>
  <svg class="abs nav-icon" style="left:1078px" width="22" height="22" viewBox="0 0 24 24" fill="none" stroke="#23150E" stroke-width="2"><path d="M3 4h3l2.4 11h10l2-8H7"/><circle cx="10" cy="19.5" r="1.4"/><circle cx="17" cy="19.5" r="1.4"/></svg>
  <svg class="abs nav-icon" style="left:1126px" width="22" height="22" viewBox="0 0 24 24" fill="none" stroke="#23150E" stroke-width="2"><circle cx="12" cy="12" r="9"/><circle cx="12" cy="10" r="3"/><path d="M6.5 18.5c3-3 8-3 11 0"/></svg>
</header>

<section class="abs hero">
  <div class="abs tag">NEW ARRIVALS JUST LANDED</div>
  <h1 class="abs head">Welcome to the <em>ultimate hub</em> for diecast collectors.</h1>
  <p class="abs">Explore a growing marketplace where you can buy, sell, or trade your favorite models. From vintage classics to modern hypercars.</p>
  <div class="abs btn-primary b1">Browse Marketplace</div>
  <div class="abs btn-ghost b2">Join the Club</div>
  <div class="abs hero-photo" role="img" aria-label="Yellow vintage diecast coupe on a dark studio background"></div>
  <div class="abs stat s1"><b>1.2k+</b><small>DAILY LISTINGS</small></div>
  <div class="abs stat s2"><b>45k+</b><small>ACTIVE COLLECTORS</small></div>
</section>

<section class="abs featured">
  <h2 class="abs head sec-title">Featured Inventory</h2>
  <p class="abs sec-sub">Curated selections from our top-rated sellers.</p>
  <div class="abs arrow" style="left:1058px"><svg width="18" height="18" viewBox="0 0 24 24" fill="none" stroke="#23150E" stroke-width="2.2"><path d="M19 12H5M11 6l-6 6 6 6"/></svg></div>
  <div class="abs arrow" style="left:1110px"><svg width="18" height="18" viewBox="0 0 24 24" fill="none" stroke="#23150E" stroke-width="2.2"><path d="M5 12h14M13 6l6 6-6 6"/></svg></div>

  <article class="abs card" style="left:47px">
    <div class="photo" role="img" aria-label="Blue sports car model in motion on a grey road" style="background:radial-gradient(ellipse 55% 18% at 50% 62%,#1E9BD0,rgba(0,0,0,0) 75%),linear-gradient(180deg,#505250,#7A7D7A 60%,#5B5D5A)">
      <span class="badge" style="background:var(--orange)">MINT CONDITION</span>
      <span class="fav"><svg width="16" height="16" viewBox="0 0 24 24" fill="none" stroke="#A8470E" stroke-width="2.2"><path d="M12 20s-7-4.5-7-10a4 4 0 017-2.5A4 4 0 0119 10c0 5.5-7 10-7 10z"/></svg></span>
    </div>
    <div class="maker">ArtMotive Performance</div>
    <h3>Valkor Sprint RS Coupe</h3>
    <div class="row"><span class="price">$185.00</span><span class="scale">1:18 Scale</span></div>
  </article>

  <article class="abs card" style="left:331px">
    <div class="photo" role="img" aria-label="Dark blue vintage roadster model on a black background" style="background:radial-gradient(ellipse 55% 20% at 50% 62%,#1F4A6A,rgba(0,0,0,0) 75%),linear-gradient(180deg,#141414,#262626)">
      <span class="badge" style="background:#C2510F">RARE FIND</span>
      <span class="fav"><svg width="16" height="16" viewBox="0 0 24 24" fill="none" stroke="#A8470E" stroke-width="2.2"><path d="M12 20s-7-4.5-7-10a4 4 0 017-2.5A4 4 0 0119 10c0 5.5-7 10-7 10z"/></svg></span>
    </div>
    <div class="maker">Korvin Heritage</div>
    <h3>1965 Hadley Adder Roadster</h3>
    <div class="row"><span class="price">$240.00</span><span class="scale">1:18 Scale</span></div>
  </article>

  <article class="abs card" style="left:615px">
    <div class="photo" role="img" aria-label="Red supercar model on a black background" style="background:radial-gradient(ellipse 50% 16% at 50% 56%,#D8361E,rgba(0,0,0,0) 75%),linear-gradient(180deg,#141414,#222)">
      <span class="badge" style="background:var(--orange)">TRENDING</span>
      <span class="fav"><svg width="16" height="16" viewBox="0 0 24 24" fill="none" stroke="#A8470E" stroke-width="2.2"><path d="M12 20s-7-4.5-7-10a4 4 0 017-2.5A4 4 0 0119 10c0 5.5-7 10-7 10z"/></svg></span>
    </div>
    <div class="maker">Braxton Models</div>
    <h3>Ferrano Vento Corsa Strada</h3>
    <div class="row"><span class="price">$510.00</span><span class="scale">1:43 Scale</span></div>
  </article>

  <article class="abs card" style="left:899px">
    <div class="photo" role="img" aria-label="Teal Japanese sports car model on a dark background" style="background:radial-gradient(ellipse 55% 22% at 50% 55%,#2B8FA3,rgba(0,0,0,0) 75%),linear-gradient(180deg,#131A1C,#1F2628)">
      <span class="badge" style="background:#2E2A28">COLLECTOR EDITION</span>
      <span class="fav"><svg width="16" height="16" viewBox="0 0 24 24" fill="none" stroke="#A8470E" stroke-width="2.2"><path d="M12 20s-7-4.5-7-10a4 4 0 017-2.5A4 4 0 0119 10c0 5.5-7 10-7 10z"/></svg></span>
    </div>
    <div class="maker">Ignara Model</div>
    <h3>Nakura Horizon Type-S</h3>
    <div class="row"><span class="price">$325.00</span><span class="scale">1:18 Scale</span></div>
  </article>
</section>

<section class="abs hub">
  <h2 class="abs head sec-title">Collector Hub Highlights</h2>
  <p class="abs sec-sub">What the circuit is talking about right now.</p>

  <article class="abs feature" role="img" aria-label="Vintage camera photographed on a dark backdrop">
    <span class="abs mc">MASTERCLASS</span>
    <h3 class="abs head">Capturing Speed: A Guide to Diecast Photography</h3>
    <div class="abs by"><i></i>By @ShutterDrift</div>
  </article>

  <article class="abs talk">
    <div class="abs corner"></div>
    <svg class="abs" style="left:30px;top:36px" width="30" height="30" viewBox="0 0 24 24" fill="none" stroke="#A8470E" stroke-width="2"><path d="M3 4h12v8H8l-4 3V4z"/><path d="M15 8h6v11l-4-3h-6v-4"/></svg>
    <h4 class="abs">Weekly Trade Discussion: JDM Classics vs. Euro Hypercars</h4>
    <p class="abs">142 Active members currently discussing their next big trades.</p>
    <a class="abs">Join Discussion <svg width="16" height="16" viewBox="0 0 24 24" fill="none" stroke="#A8470E" stroke-width="2.2"><path d="M5 12h14M13 6l6 6-6 6"/></svg></a>
  </article>

  <article class="abs mini-card verify">
    <div class="abs ic" style="background:var(--sand)"><svg width="18" height="18" viewBox="0 0 24 24" fill="none" stroke="#A8470E" stroke-width="2.2"><circle cx="12" cy="12" r="8"/><path d="M8.5 12l2.5 2.5 4.5-5"/></svg></div>
    <span class="abs lab">AUTHENTICATION</span>
    <h5 class="abs">New Verified Seller Badge Program</h5>
    <p class="abs" style="color:var(--muted)">Secure your reputation in the community with our new 5-step verification process.</p>
  </article>

  <article class="abs mini-card summit">
    <div class="abs ic" style="background:rgba(255,255,255,.2)"><svg width="18" height="18" viewBox="0 0 24 24" fill="none" stroke="#fff" stroke-width="2"><rect x="4" y="5" width="16" height="15" rx="2"/><path d="M4 10h16M8 3v4M16 3v4"/></svg></div>
    <h5 class="abs" style="color:#fff">Annual Collector Summit 2024</h5>
    <p class="abs" style="color:#F5D3BC">Save the date! We're gathering the world's top diecast enthusiasts in Las Vegas.</p>
    <div class="abs reg">REGISTER NOW</div>
  </article>
</section>

<section class="abs cta">
  <h2 class="head">Ready to join the circuit?</h2>
  <p>Join over 45,000 passionate collectors. Get early access to exclusive drops, verified authentication services, and the world's most vibrant diecast trading floor.</p>
  <div class="abs btn-primary c1">CREATE YOUR ACCOUNT</div>
  <div class="abs c2">Explore Marketplace</div>
</section>

<footer>
  <div class="abs foot-logo">BRIMBLE</div>
  <p class="abs foot-about">The premier editorial marketplace for serious diecast enthusiasts. Precision engineering meets high-end collecting.</p>
  <div class="abs foot-social">
    <svg width="20" height="20" viewBox="0 0 24 24" fill="none" stroke="#5B4A40" stroke-width="1.8"><circle cx="12" cy="12" r="9"/><path d="M3 12h18M12 3c3 3 3 15 0 18M12 3c-3 3-3 15 0 18"/></svg>
    <svg width="20" height="20" viewBox="0 0 24 24" fill="none" stroke="#5B4A40" stroke-width="1.8"><circle cx="12" cy="12" r="4"/><path d="M16 12v1.5a2.5 2.5 0 005 0V12a9 9 0 10-3.5 7.1"/></svg>
    <svg width="20" height="20" viewBox="0 0 24 24" fill="none" stroke="#5B4A40" stroke-width="1.8"><path d="M3 4h12v8H8l-4 3V4z"/><path d="M15 8h6v11l-4-3h-6v-4"/></svg>
  </div>
  <div class="abs foot-col" style="left:334px"><h6>PLATFORM</h6><ul><li>Marketplace</li><li>Collector Hub</li><li>Price Guide</li><li>Verified Sellers</li></ul></div>
  <div class="abs foot-col" style="left:622px"><h6>COMMUNITY</h6><ul><li>About Us</li><li>Community Guidelines</li><li>Snapwall</li><li>Chatterhall</li></ul></div>
  <div class="abs foot-col" style="left:911px"><h6>SUPPORT</h6><ul><li>Help Center</li><li>Shipping &amp; Returns</li><li>Privacy Policy</li><li>Terms of Service</li></ul></div>
  <div class="abs foot-bottom"><span>© 2024 BRIMBLE DIECAST. THE CURATED CIRCUIT.</span><span class="right"><span>PRECISION DRIVEN</span><span>EXPERTLY CURATED</span></span></div>
</footer>

</body>
</html>
```